Bartley's Harbor Grill (New Website Design)

I want an upgraded, modern, sleek, tasteful website that is easily updated internally. Our current website can be viewed at www.bartleysharborgrill.example

Target Market(s)

Dining Customers

Industry/Entity Type

Restaurant / Hospitality

Coding

Coded - Design and coding required

Number of Pages Required

4 page

Requirements
Must have
• Modern, artful, sleek.. while maintaining a little vintage Cape Cod

```html
<!DOCTYPE html>
<html lang="en">
<head>
<meta charset="utf-8">
<title>Bartley's Harbor Grill</title>
<link href="https://fonts.googleapis.com/css2?family=Poppins:ital,wght@0,400;0,500;0,600;1,300;1,400&display=swap" rel="stylesheet">
<style>
:root{
  --teal:#243c48;
  --teal-deep:#1d333e;
  --orange:#c1680c;
  --white:#ffffff;
  --ink:#1f2a30;
  --muted:#6b7478;
  --star:#f2a60c;
}
*{box-sizing:border-box;margin:0;padding:0}
html,body{width:1200px;height:4562px;overflow:hidden}
body{position:relative;background:var(--teal);font-family:'Poppins',sans-serif;color:var(--white)}
.abs{position:absolute}
a{color:inherit;text-decoration:none}

/* header */
.brand{left:98px;top:22px;width:90px;font-size:15px;font-weight:500;line-height:1.15;text-align:center}
.nav{left:245px;top:38px;display:flex;gap:29px;font-size:18px}
.nav .active{text-decoration:underline;text-underline-offset:4px}
.btn{display:flex;align-items:center;justify-content:center;background:var(--orange);color:var(--white);border-radius:30px;font-weight:500}
.contact-btn{left:982px;top:25px;width:134px;height:50px;font-size:18px}

/* hero */
.hero-title{left:88px;top:236px;font-size:34px;font-weight:600}
.hero-text{left:88px;top:300px;width:470px;font-size:19.5px;line-height:1.5}
.hero-btn{left:83px;top:441px;width:200px;height:52px;font-size:17.5px}
.hero-photo{left:621px;top:138px;width:494px;height:552px;background:radial-gradient(circle at 50% 55%,#6b7a45 0,#2e3a2a 35%,#1b1e1c 70%)}

/* specials */
.specials{left:0;top:690px;width:1200px;height:386px;background:var(--orange)}
.section-title{width:1200px;left:0;text-align:center;font-size:29px;font-weight:500}
.spec-card{top:843px;width:193px;height:191px;background:var(--white);border-radius:8px;color:var(--ink);text-align:center;font-size:16px;line-height:1.55;padding-top:126px}
.spec-card.featured{background:var(--teal);color:var(--white)}
.spec-icon{position:absolute;left:61px;top:22px;width:72px;height:72px;border-radius:50%}

/* food */
.sub{width:1200px;left:0;text-align:center;font-size:20px;line-height:1.5}
.food-card{width:322px;height:352px;background:var(--white);border-radius:8px;overflow:hidden;color:var(--ink)}
.food-card.featured{background:var(--orange);color:var(--white)}
.food-photo{height:216px}
.food-card h3{font-size:20px;font-weight:500;margin:22px 20px 6px}
.food-card p{font-size:15.5px;line-height:1.6;margin:0 20px;width:200px;color:var(--muted)}
.food-card.featured p{color:var(--white)}
.more-btn{left:535px;top:2137px;width:129px;height:52px;font-size:17.5px}

/* chefs */
.chef{width:234px}
.chef-photo{height:370px;border-radius:6px}
.chef h3{font-size:23px;font-weight:600;margin-top:16px}
.chef p{font-size:19px;margin-top:12px}

/* reviews */
.reviews{left:0;top:3087px;width:1200px;height:414px;background:var(--orange)}
.arrow{top:3247px}
.review{top:3297px;width:399px;height:349px;background:var(--white);border-radius:22px;color:var(--ink);text-align:center}
.avatar{position:absolute;top:20px;width:62px;height:62px;border-radius:50%;background:#8a8f92}
.review .who{position:absolute;top:38px;font-size:21px}
.review blockquote{position:absolute;left:50px;top:130px;width:300px;font-size:21px;font-style:italic;font-weight:300;line-height:1.55;color:var(--muted)}
.stars{position:absolute;left:0;top:275px;width:399px;text-align:center;color:var(--star);font-size:32px;letter-spacing:8px}

/* suggestions */
.suggest{left:0;top:3737px;width:1200px;height:325px;background:linear-gradient(120deg,#5b6a63,#8e8a72 45%,#6f7b7d 75%,#a3a6a0)}
.suggest-title{left:0;width:1200px;top:3780px;text-align:center;font-size:29px;font-weight:600;line-height:1.45}
.mail{left:331px;top:3919px;width:536px;height:74px;border-radius:40px;background:rgba(120,120,110,.55);border:1px solid rgba(255,255,255,.35)}
.mail span{position:absolute;left:38px;top:20px;font-size:24px}
.send{left:697px;top:3919px;width:170px;height:74px;font-size:22px;border-radius:40px}

/* footer */
.foot-brand{left:94px;top:4150px;font-size:28px;font-weight:500}
.foot-text{left:86px;top:4288px;width:340px;font-size:19.5px;line-height:1.55}
.col h4{font-size:20px;font-weight:600;margin-bottom:20px}
.col li{list-style:none;font-size:17.5px;margin-bottom:16px}
.social li{display:flex;align-items:center;gap:14px;margin-bottom:22px}
.social .dot{width:38px;height:38px;border-radius:50%;background:var(--white)}
.rule{left:86px;top:4489px;width:1032px;height:1px;background:rgba(255,255,255,.7)}
.legal{left:0;width:1200px;top:4510px;text-align:center;font-size:19.5px;font-weight:500}
</style>
</head>
<body>

<header>
  <div class="abs brand">Bartley's Harbor Grill</div>
  <nav class="abs nav">
    <a class="active">Order online</a><a class="active">Our menu</a><a>Seafood marketpleace</a><a>Gift card</a><a>About us</a>
  </nav>
  <a class="abs btn contact-btn">Contact us</a>
</header>

<section class="hero">
  <h1 class="abs hero-title">Welcome to Bartley's</h1>
  <p class="abs hero-text">Established in 1938, Bartley's Restaurant offers classic Cape Cod fare featuring fresh seafood and creative comfort cuisine.</p>
  <a class="abs btn hero-btn">Reservations Now</a>
  <div class="abs hero-photo" role="img" aria-label="Plated egg, avocado and greens on toast on a dark board"></div>
</section>

<section>
  <div class="abs specials"></div>
  <h2 class="abs section-title" style="top:742px">Special menu at the cafe</h2>
  <div class="abs spec-card" style="left:83px"><div class="spec-icon" style="background:#f0823a" role="img" aria-label="Shrimp illustration"></div>Shrimp with<br>oyster sauce</div>
  <div class="abs spec-card" style="left:294px"><div class="spec-icon" style="background:#f28c2e" role="img" aria-label="Crab illustration"></div>Crab with oyster<br>sauce</div>
  <div class="abs spec-card featured" style="left:503px"><div class="spec-icon" style="background:#f6a21c" role="img" aria-label="Fish illustration"></div>Fish with oyster<br>sauce</div>
  <div class="abs spec-card" style="left:713px"><div class="spec-icon" style="background:#e2432e" role="img" aria-label="Lobster illustration"></div>Lobster with<br>oyster sauce</div>
  <div class="abs spec-card" style="left:922px"><div class="spec-icon" style="background:#f0823a" role="img" aria-label="Shrimp illustration"></div>Shrimp with<br>oyster sauce</div>
</section>

<section>
  <h2 class="abs section-title" style="top:1132px">Food provided by us</h2>
  <p class="abs sub" style="top:1190px">We recommend several foods that you can eat when you come<br>to the restaurant</p>

  <article class="abs food-card" style="left:83px;top:1331px"><div class="food-photo" style="background:linear-gradient(135deg,#3a2a1e,#c98a4f 50%,#2b2b2b)" role="img" aria-label="Pan of garlic prawns"></div><h3>Prawns are delicious</h3><p>Special dishes from our chef</p></article>
  <article class="abs food-card featured" style="left:439px;top:1331px"><div class="food-photo" style="background:linear-gradient(135deg,#6a6a6a,#d8a06a 50%,#2f2f33)" role="img" aria-label="Bowl of shrimp fried rice"></div><h3>Shrimp fried rice</h3><p>Special dishes from our chef</p></article>
  <article class="abs food-card" style="left:795px;top:1331px"><div class="food-photo" style="background:radial-gradient(circle at 55% 55%,#2a2a2a 0,#6d6a63 25%,#e9e4de 50%)" role="img" aria-label="Plate of fresh mussels with lemon"></div><h3>Fresh mussels</h3><p>Special dishes from our chef</p></article>

  <article class="abs food-card" style="left:83px;top:1726px"><div class="food-photo" style="background:linear-gradient(135deg,#2a2a2a,#c8512e 40%,#e5c9a3 70%,#2a2a2a)" role="img" aria-label="Grilled lobster dish"></div><h3>Lobster dish</h3><p>Special dishes from our chef</p></article>
  <article class="abs food-card" style="left:439px;top:1726px"><div class="food-photo" style="background:linear-gradient(135deg,#5d5a52,#c77a3a 50%,#3a3c32)" role="img" aria-label="Crab in oyster sauce"></div><h3>Oyster sauce crab</h3><p>Special dishes from our chef</p></article>
  <article class="abs food-card" style="left:795px;top:1726px"><div class="food-photo" style="background:linear-gradient(135deg,#5a3a22,#e8734a 50%,#3a2a1e)" role="img" aria-label="Smoked salmon toasts"></div><h3>Prawns are delicious</h3><p>Special dishes from our chef</p></article>

  <a class="abs btn more-btn">View More</a>
</section>

<section>
  <h2 class="abs section-title" style="top:2254px">our chef's experience was truly amazing</h2>
  <p class="abs sub" style="top:2311px">We present chefs who are experienced in their fields and can<br>make the taste of dishes different</p>
  <div class="abs chef" style="left:83px;top:2535px"><div class="chef-photo" style="background:linear-gradient(180deg,#6b4a2e,#2a2420)" role="img" aria-label="Chef cooking under copper lamps"></div><h3>Chef Marco</h3><p>2 years experience</p></div>
  <div class="abs chef" style="left:349px;top:2437px"><div class="chef-photo" style="background:linear-gradient(180deg,#8a7b6c,#7a2a2a)" role="img" aria-label="Chef in red apron"></div><h3>Chef Dalton</h3><p>5 years experience</p></div>
  <div class="abs chef" style="left:616px;top:2535px"><div class="chef-photo" style="background:linear-gradient(180deg,#d9d9d9,#f1f1f1)" role="img" aria-label="Chef in white jacket"></div><h3>Chef Ellis</h3><p>3 years experience</p></div>
  <div class="abs chef" style="left:883px;top:2437px"><div class="chef-photo" style="background:linear-gradient(180deg,#cfcfcf,#4a4a4a)" role="img" aria-label="Chef with arms crossed in apron"></div><h3>Chef Kenji</h3><p>3 years experience</p></div>
</section>

<section>
  <div class="abs reviews"></div>
  <h2 class="abs section-title" style="top:3130px;font-size:29px;font-weight:400;line-height:1.45">Evaluation of our cafe from customers who<br>have made reservations at our cafe</h2>
  <svg class="abs arrow" style="left:70px" width="26" height="22" viewBox="0 0 26 22" fill="none" stroke="rgba(255,255,255,.6)" stroke-width="2.5"><path d="M24 11H3M11 3 3 11l8 8"/></svg>
  <svg class="abs arrow" style="left:134px" width="26" height="22" viewBox="0 0 26 22" fill="none" stroke="#fff" stroke-width="2.5"><path d="M2 11h21M15 3l8 8-8 8"/></svg>

  <article class="abs review" style="left:67px"><div class="avatar" style="left:128px" role="img" aria-label="Customer portrait"></div><span class="who" style="left:212px">Nora</span><blockquote>“Eating at this restaurant takes me back to my childhood with classic seafood dishes”</blockquote><div class="stars">★★★★★</div></article>
  <article class="abs review" style="left:501px"><div class="avatar" style="left:118px" role="img" aria-label="Customer portrait"></div><span class="who" style="left:200px">Felix</span><blockquote>“It's very delicious to eat here as if I were eating at my mother's house”</blockquote><div class="stars">★★★★★</div></article>
  <article class="abs review" style="left:934px"><div class="avatar" style="left:126px" role="img" aria-label="Customer portrait"></div><span class="who" style="left:210px">Maren</span><blockquote>“The tastiest seafood at a cheap price, I recommend going to this restaurant”</blockquote><div class="stars">★★★★★</div></article>
</section>

<section>
  <div class="abs suggest" role="img" aria-label="Table spread of clam pasta dishes, softly dimmed"></div>
  <h2 class="abs suggest-title">Send suggestions for dishes or our services<br>that you find unsatisfactory via email</h2>
  <div class="abs mail"><span>Email</span></div>
  <a class="abs btn send">Send</a>
</section>

<footer>
  <div class="abs foot-brand">Bartley's</div>
  <p class="abs foot-text">Established in 1938, Bartley's Restaurant offers classic Cape Cod fare featuring fresh seafood and creative comfort cuisine.</p>
  <div class="abs col" style="left:556px;top:4168px"><h4>Info</h4><ul><li>Our menu</li><li>Gift card</li><li>Testimonials</li><li>About us</li></ul></div>
  <div class="abs col" style="left:717px;top:4168px"><h4>Company</h4><ul><li>Galery</li><li>News</li><li>Contact us</li><li>Connect</li></ul></div>
  <div class="abs col social" style="left:869px;top:4168px"><h4>Find us on social media</h4><ul><li><span class="dot"></span>Social feed</li><li><span class="dot"></span>Photo stream</li><li><span class="dot"></span>Short posts</li></ul></div>
  <div class="abs rule"></div>
  <p class="abs legal">All Right Reserved / Privacy Policy / Termn and use</p>
</footer>

</body>
</html>
```